Business Card Re-design

We are looking for a fresh bold look for general office business cards. We are a staffing agency that staffs industrial, coal mining, and clerical jobs.
Tag Line: We match the RIGHT talent with the RIGHT roles.
Harlow Falls Office: 2473 W. Tallow Creek Rd, Harlow Falls, OH - 47308
p. 555.203.6180 f. 555.203.6195
Brookmere Office: 264 S. Birch Ln, Brookmere, OH - 47152
p. 555.319.2047 f. 555.203.6195
Absentee/Emergency 24hr Hotline 555.203.6172 opt.1
www.bluelanternworkforce.example

```html
<!DOCTYPE html>
<html lang="en">
<head>
<meta charset="utf-8">
<title>Blue Lantern Workforce – Business Card</title>
<link rel="stylesheet" href="https://fonts.googleapis.com/css2?family=Montserrat:wght@400;500;700;800&display=swap">
<style>
  :root {
    --navy: #1f4a6b;
    --green: #3a9a47;
    --paper: #f6f6f6;
    --backdrop: #e9e9e9;
    --ink: #2b2b2b;
    --white: #ffffff;
  }
  * { box-sizing: border-box; margin: 0; padding: 0; }
  html, body {
    width: 1200px; height: 1137px; overflow: hidden;
    background: var(--backdrop);
    font-family: "Montserrat", sans-serif;
  }
  .sheet {
    position: relative; width: 1200px; height: 1137px;
    display: flex; align-items: center; justify-content: center; gap: 48px;
  }
  .card { box-shadow: 0 6px 18px rgba(0,0,0,0.12); overflow: hidden; }

  /* Front: portrait */
  .card-front {
    width: 360px; height: 630px; background: var(--paper);
    display: flex; flex-direction: column;
  }
  .front-identity {
    height: 55%; display: flex; flex-direction: column;
    align-items: center; justify-content: center; gap: 70px;
    border-bottom: 4px solid var(--green);
  }
  .brand-mark { display: flex; align-items: center; gap: 10px; }
  .brand-square { width: 18px; height: 18px; background: var(--navy); flex: none; }
  .brand-name {
    font-weight: 800; font-size: 22px; line-height: 1.1;
    color: var(--navy); text-transform: uppercase; letter-spacing: 0.5px;
  }
  .person { text-align: center; }
  .person-name { color: var(--green); font-weight: 800; font-size: 24px; }
  .person-title { color: var(--ink); font-size: 12px; font-weight: 500; margin-top: 2px; }

  .front-contact {
    flex: 1; background: var(--navy); color: var(--white);
    display: flex; flex-direction: column; justify-content: center;
    align-items: center; text-align: center; gap: 16px; padding: 0 18px;
    font-size: 12px; line-height: 1.45;
  }
  .office-name { font-weight: 700; font-size: 14px; }
  .label { font-weight: 700; }
  .web { font-size: 12px; }

  /* Back: landscape */
  .card-back {
    width: 630px; height: 360px; background: var(--navy); color: var(--white);
    display: flex; flex-direction: column; align-items: center; justify-content: center; gap: 22px;
  }
  .card-back .brand-square { background: var(--white); width: 24px; height: 24px; }
  .card-back .brand-name { color: var(--white); font-size: 34px; }
  .tagline { font-size: 17px; line-height: 1.35; text-align: center; font-weight: 400; }
  .tagline strong { font-weight: 800; }
</style>
</head>
<body>
<main class="sheet">
  <section class="card card-front" aria-label="Business card front">
    <div class="front-identity">
      <div class="brand-mark">
        <span class="brand-square"></span>
        <span class="brand-name">Blue Lantern<br>Workforce</span>
      </div>
      <div class="person">
        <p class="person-name">Daniel REYES</p>
        <p class="person-title">Managing Director</p>
      </div>
    </div>
    <div class="front-contact">
      <div class="office">
        <p class="office-name">Harlow Falls Office</p>
        <p>2473 W. Tallow Creek Rd, Harlow Falls, OH-47308</p>
        <p><span class="label">P</span> 555.203.6180 • <span class="label">F</span> 555.203.6195</p>
      </div>
      <div class="office">
        <p class="office-name">Brookmere Office</p>
        <p>264 S. Birch Ln, Brookmere, OH-47152</p>
        <p><span class="label">P</span> 555.319.2047 • <span class="label">F</span> 555.203.6195</p>
      </div>
      <div class="office">
        <p class="office-name">Absentee/Emergency</p>
        <p><span class="label">24hr Hotline</span> 555.203.6172 opt.1</p>
        <p class="web">www.bluelanternworkforce.example</p>
      </div>
    </div>
  </section>

  <section class="card card-back" aria-label="Business card back">
    <div class="brand-mark">
      <span class="brand-square"></span>
      <span class="brand-name">Blue Lantern Workforce</span>
    </div>
    <p class="tagline">We match the <strong>RIGHT</strong> talent<br>with the <strong>RIGHT</strong> roles.</p>
  </section>
</main>
</body>
</html>
```